Presentation Folder, Business Card, Letterhead and Envelope design

We are a dental clinic that will open in August and we are looking for a professional graphic designer to create our Business Card, Presentation Folder, Letterhead, Notepad and envelopes.

The brand LumaGrin must reflect a sense of quality and sophistication, marketed for middle-class consumers.
Our preference is for quality and refined materials, where less is more.
Attached the logo

```html
<!DOCTYPE html>
<html lang="en">
<head>
<meta charset="utf-8">
<title>LumaGrin Business Card</title>
<link rel="stylesheet" href="https://fonts.googleapis.com/css2?family=Questrial&family=Montserrat:wght@700&display=swap">
<style>
  :root {
    --backdrop: #3b3b3d;
    --card-dark: #58585a;
    --card-light: #ffffff;
    --ink-gray: #555557;
    --ink-soft: #6a6a6c;
    --wine: #6e1212;
    --line: #c9c9c9;
  }
  * { box-sizing: border-box; margin: 0; padding: 0; }
  html, body { width: 1200px; height: 1000px; overflow: hidden; }
  body {
    background: var(--backdrop);
    font-family: "Questrial", sans-serif;
    position: relative;
  }
  .card {
    position: absolute;
    width: 600px;
    height: 343px;
    border-radius: 26px;
    overflow: hidden;
  }

  /* Front */
  .card-front {
    left: 50px; top: 90px;
    background: var(--card-dark);
  }
  .card-front .frame {
    position: absolute; inset: 14px;
    border: 2px solid #e8e8e8;
    border-radius: 18px;
  }
  .card-front .brand {
    position: absolute; left: 0; right: 0; top: 0; bottom: 0;
    display: flex; flex-direction: column; align-items: center; justify-content: center; gap: 26px;
  }
  .card-front .brand-square {
    width: 70px; height: 70px; background: var(--card-light);
  }
  .card-front .brand-name {
    color: var(--card-light);
    font-size: 58px; letter-spacing: 8px; line-height: 1;
  }

  /* Back */
  .card-back {
    left: 550px; top: 500px;
    background: var(--card-light);
  }
  .card-back .top-band {
    position: absolute; left: 0; right: 0; top: 0; height: 20px;
    background: var(--wine);
  }
  .card-back .brand {
    position: absolute; left: 40px; top: 50px;
    display: flex; align-items: center; gap: 18px;
  }
  .card-back .brand-square {
    width: 56px; height: 56px; background: var(--ink-gray);
  }
  .card-back .brand-name {
    color: var(--ink-gray);
    font-size: 60px; letter-spacing: 9px; line-height: 1;
  }
  .card-back .person {
    position: absolute; right: 330px; top: 150px;
    text-align: right; width: 260px;
  }
  .person-name {
    font-family: "Montserrat", sans-serif; font-weight: 700;
    color: var(--ink-gray); font-size: 24px; letter-spacing: 0.5px;
  }
  .person-role { color: var(--wine); font-size: 16px; margin-top: 4px; }
  .person-address { color: var(--ink-soft); font-size: 15px; line-height: 1.5; margin-top: 14px; }
  .card-back .divider {
    position: absolute; left: 290px; top: 140px; width: 1px; height: 150px;
    background: var(--line);
  }
  .contacts {
    position: absolute; left: 310px; top: 148px;
    list-style: none; display: flex; flex-direction: column; gap: 12px;
  }
  .contact {
    display: flex; align-items: center; gap: 14px;
    color: var(--ink-soft); font-size: 16px;
  }
  .contact .accent { color: var(--wine); }
  .contact-icon {
    width: 24px; height: 24px; border: 1px solid #bdbdbd; border-radius: 4px;
    display: flex; align-items: center; justify-content: center;
  }
  .contact-icon svg { width: 16px; height: 16px; fill: var(--wine); }
</style>
</head>
<body>

<section class="card card-front" aria-label="Business card front">
  <div class="frame"></div>
  <div class="brand">
    <div class="brand-square"></div>
    <div class="brand-name">LUMAGRIN</div>
  </div>
</section>

<section class="card card-back" aria-label="Business card back">
  <div class="top-band"></div>
  <div class="brand">
    <div class="brand-square"></div>
    <div class="brand-name">LUMAGRIN</div>
  </div>

  <div class="person">
    <div class="person-name">YOUR DESIGN</div>
    <div class="person-role">Managing Director</div>
    <div class="person-address">01, LumaGrin Clinic, Your Street,<br>Your Country Code - 12345</div>
  </div>

  <div class="divider"></div>

  <ul class="contacts">
    <li class="contact">
      <span class="contact-icon"><svg viewBox="0 0 16 16"><path d="M2 6c0-2 2-3 6-3s6 1 6 3v1h-3V5.5H5V7H2z"/><rect x="3" y="8" width="10" height="6" rx="1"/></svg></span>
      012 3456 789
    </li>
    <li class="contact">
      <span class="contact-icon"><svg viewBox="0 0 16 16"><rect x="4" y="1" width="8" height="5"/><rect x="1" y="6" width="14" height="6" rx="1"/><rect x="4" y="10" width="8" height="5" fill="#fff" stroke="#6e1212"/></svg></span>
      012 3456 780
    </li>
    <li class="contact">
      <span class="contact-icon"><svg viewBox="0 0 16 16"><rect x="1" y="3" width="14" height="10"/><path d="M1 3l7 6 7-6" fill="none" stroke="#fff" stroke-width="1.3"/></svg></span>
      info@lumagrin.com
    </li>
    <li class="contact">
      <span class="contact-icon"><svg viewBox="0 0 16 16"><circle cx="8" cy="8" r="7"/><path d="M1 8h14M8 1v14M3 4h10M3 12h10" stroke="#fff" stroke-width="1" fill="none"/><ellipse cx="8" cy="8" rx="3" ry="7" fill="none" stroke="#fff"/></svg></span>
      www.<span class="accent">lumagrin</span>.com
    </li>
  </ul>
</section>

</body>
</html>
```